New business Cards

We need some new cards that stand out. We love our logo and colour scheme but need to incorporate a qubo logo and bfn logo yet still keep our cards uncluttered and clean looking.
Our tag is Bright Ledger. Anywhere, Anytime.
The idea of the cards is to show authority in accounting and Qubo/ cloud software

```html
<!DOCTYPE html>
<html lang="en">
<head>
<meta charset="utf-8">
<title>Marlow Business Solutions – Business Cards</title>
<link rel="stylesheet" href="https://fonts.googleapis.com/css2?family=Source+Sans+3:wght@400;600&display=swap">
<style>
  :root {
    --stage: #ecebe8;
    --card-white: #ffffff;
    --card-black: #0d0d0d;
    --card-black-soft: #1c1c1c;
    --brand-green: #6cbf4f;
    --text-dark: #1e1e1e;
    --text-mid: #3a3a3a;
    --badge-neutral: #d9d9d6;
  }
  * { box-sizing: border-box; margin: 0; padding: 0; }
  html, body { width: 1200px; height: 784px; overflow: hidden; }
  body {
    background: var(--stage);
    font-family: "Source Sans 3", "Myriad Pro", sans-serif;
    position: relative;
  }
  .card {
    position: absolute;
    width: 560px;
    height: 320px;
    box-shadow: 0 6px 18px rgba(0,0,0,0.18);
    overflow: hidden;
  }

  /* Back of card */
  .card-back {
    left: 70px; top: 80px;
    background: radial-gradient(ellipse at 50% 35%, var(--card-black-soft), var(--card-black) 75%);
    color: var(--brand-green);
  }
  .card-back .brand {
    position: absolute; left: 0; right: 0; top: 92px;
    display: flex; justify-content: center; align-items: center; gap: 14px;
  }
  .brand-square { width: 46px; height: 46px; background: var(--brand-green); }
  .brand-name {
    font-weight: 600; font-size: 30px; letter-spacing: 1px;
    line-height: 1; color: var(--brand-green);
  }
  .card-back .tagline {
    position: absolute; left: 0; right: 0; bottom: 54px;
    text-align: center;
    font-size: 17px; letter-spacing: 5px; text-transform: uppercase;
    color: var(--brand-green);
  }

  /* Front of card */
  .card-front {
    left: 570px; top: 384px;
    background: var(--card-white);
  }
  .card-front .brand {
    position: absolute; left: 30px; top: 28px;
    display: flex; align-items: center; gap: 12px;
  }
  .card-front .brand-square { width: 38px; height: 38px; }
  .card-front .brand-name { font-size: 24px; }
  .holder { position: absolute; left: 30px; top: 104px; }
  .holder-name { font-size: 20px; color: var(--brand-green); font-weight: 400; }
  .holder-role { font-size: 14px; color: var(--text-mid); margin-top: 1px; }
  .contact-list { position: absolute; left: 30px; top: 164px; list-style: none; }
  .contact-list li {
    display: flex; align-items: center; gap: 8px;
    font-size: 15px; color: var(--text-dark); line-height: 21px;
  }
  .contact-list svg { width: 14px; height: 14px; flex: none; }
  .contact-list .no-icon { padding-left: 22px; }
  .partner-badges {
    position: absolute; right: 26px; top: 100px;
    display: flex; flex-direction: column; align-items: flex-end; gap: 8px;
  }
  .badge-plain {
    width: 64px; height: 30px; background: var(--badge-neutral);
  }
  .footer-rule {
    position: absolute; left: 0; right: 0; bottom: 40px;
    height: 4px; background: var(--brand-green);
  }
  .footer-band {
    position: absolute; left: 0; right: 0; bottom: 0; height: 38px;
    background: var(--card-black);
    color: var(--card-white);
    font-size: 14px; letter-spacing: 6px; text-transform: uppercase;
    display: flex; align-items: center; justify-content: center;
  }
</style>
</head>
<body>

<section class="card card-back" aria-label="Card back">
  <div class="brand">
    <span class="brand-square"></span>
    <span class="brand-name">Marlow Business Solutions</span>
  </div>
  <p class="tagline">Bright Ledger. Anywhere, Anytime.</p>
</section>

<section class="card card-front" aria-label="Card front">
  <div class="brand">
    <span class="brand-square"></span>
    <span class="brand-name">Marlow Business Solutions</span>
  </div>

  <div class="holder">
    <p class="holder-name">Elena Marlow, BFN, CTA</p>
    <p class="holder-role">Partner</p>
  </div>

  <ul class="contact-list">
    <li>
      <svg viewBox="0 0 24 24" aria-hidden="true"><path fill="#6cbf4f" d="M6.6 10.8a15.1 15.1 0 0 0 6.6 6.6l2.2-2.2a1 1 0 0 1 1-.25 11.4 11.4 0 0 0 3.6.57 1 1 0 0 1 1 1V20a1 1 0 0 1-1 1A17 17 0 0 1 3 4a1 1 0 0 1 1-1h3.5a1 1 0 0 1 1 1c0 1.250.2 2.45.57 3.57a1 1 0 0 1-.25 1z"/></svg>
      03 5550 1827
    </li>
    <li>
      <svg viewBox="0 0 24 24" aria-hidden="true"><path fill="#6cbf4f" d="M3 5h18v14H3z"/><path fill="none" stroke="#fff" stroke-width="2" d="M3 6l9 7 9-7"/></svg>
      elenam@marlowbizsol.com.au
    </li>
    <li>
      <svg viewBox="0 0 24 24" aria-hidden="true"><circle cx="12" cy="12" r="10" fill="#6cbf4f"/><path fill="none" stroke="#fff" stroke-width="1.5" d="M2 12h20M12 2c3 3 3 17 0 20M12 2c-3 3-3 17 0 20"/></svg>
      www.marlowbizsol.com.au
    </li>
    <li class="no-icon">Brookfield Vic 3999</li>
  </ul>

  <div class="partner-badges" aria-label="Partner accreditations">
    <span class="badge-plain"></span>
    <span class="badge-plain"></span>
  </div>

  <div class="footer-rule"></div>
  <div class="footer-band">Bright Ledger. Anywhere, Anytime.</div>
</section>

</body>
</html>
```